Design website home page for pathology consulting company

Starting a new consulting company with anatomic pathologists focused on expert diagnosis and second opinions on difficult pathology cases. In the near future we will be incorporating next generation diagnostics for rare diseases of childhood into the business. These include discovery and testing of DNA for mutations.

The company is formed around one of the best known pathologists in the world named Harold "Juniper" Tolvik. The name of the company is "JuniperLab"

We had a logo design by ArtfulHive - it is great. I will attach file as soon as I have it (contest ending today). Our company is medical, uses microscopes, DNA, probably will focus on childhood diseases but not solely on childhood diseases. we're not particularly conservative, but the customers we want to appeal to include older practicing pathologists as well as patients (sometimes parents) looking for second opinions.

Think a group of expert doctors diagnosing disease through the microscope and through DNA technology, ages ranging from 35-75 all trained by the best pathologist in the world - "Juniper"

We receive glass slides from diseases from patients all over the world from docs who need an expert to tell them what is the diagnosis. So "path to the diagnosis" is also part of the company marketing message.

We want the website design to describe our company but be very simple to find what one is looking for as we will use it as the launch page to:
1) order services
2) check results/reports
3) set up new account
4) speak with one of the pathologists
5) see our test menu
6) access our educational material/webinars
Updates

Update - looking for home page design and then finalists will ask for second page design to keep with theme - ok?

Reason: realized this project isn't web design but web home page design - thanks

Reason: Holidays for some in next two weeks

Reason: Hot discussion among collaborators for a few of the submissions. Will provide detail individually this weekend. Thanks so much for all the submissions!

Target Market(s)

Referring pathologists, physicians who want second opinions on pathology disease diagnosis, patients who have had biopsies (either patients themselves or parents of patients), generally high education level

Industry/Entity Type

Marketing

Requirements
Must have
• JuniperLab
Next Generation Pathology Consultants

```html
<!DOCTYPE html>
<html lang="en">
<head>
<meta charset="utf-8">
<title>JuniperLab – Next Generation Pathology Consultants</title>
<link rel="stylesheet" href="https://fonts.googleapis.com/css2?family=Open+Sans:ital,wght@0,300;0,400;0,600;1,300&display=swap">
<style>
  :root {
    --brand-blue: #1a7fc1;
    --nav-active: #1a8fd6;
    --line-blue: #1f7dbf;
    --tile-sky: #3eb0e4;
    --tile-ocean: #178ed5;
    --tile-indigo: #3a59b3;
    --tile-violet: #6a4fc1;
    --date-blue: #3ba4dd;
    --text-dark: #2b2b2b;
    --text-body: #444;
    --text-muted: #9a9a9a;
    --nav-grey: #a8a8a8;
    --icon-grey: #d2d2d2;
    --input-border: #e2e2e2;
    --white: #ffffff;
  }
  * { box-sizing: border-box; margin: 0; padding: 0; }
  html, body { width: 857px; height: 1200px; overflow: hidden; }
  body {
    position: relative;
    background: var(--white);
    font-family: "Open Sans", Arial, sans-serif;
    font-weight: 300;
    color: var(--text-body);
  }
  .abs { position: absolute; }

  /* header */
  .brand { left: 34px; top: 22px; width: 170px; text-align: center; }
  .brand-mark { display: block; width: 60px; height: 60px; margin: 0 auto 6px; border-radius: 50%; background: var(--brand-blue); }
  .brand-name { font-size: 28px; font-weight: 400; color: var(--brand-blue); letter-spacing: 0.5px; line-height: 1; }
  .brand-tagline { font-size: 8.5px; font-weight: 400; color: var(--brand-blue); margin-top: 4px; white-space: nowrap; }

  .social { top: 14px; left: 600px; display: flex; gap: 8px; }
  .social span { width: 20px; height: 20px; background: var(--icon-grey); border-radius: 2px; }
  .account-links { top: 16px; right: 10px; font-size: 12px; font-weight: 400; color: var(--brand-blue); letter-spacing: 0.4px; }
  .account-links .sep { margin: 0 6px; }

  .main-nav { top: 66px; left: 246px; display: flex; font-size: 12.5px; font-weight: 400; letter-spacing: 0.3px; }
  .main-nav a { display: block; height: 34px; line-height: 34px; padding: 0 12px; margin-right: 14px; color: var(--nav-grey); text-decoration: none; }
  .main-nav a.active { background: var(--nav-active); color: var(--white); }

  .header-rule { left: 0; top: 128px; width: 857px; height: 6px; background: var(--line-blue); }

  /* hero */
  .hero { left: 0; top: 134px; width: 857px; height: 286px;
    background: linear-gradient(90deg, #7fb3d6 0%, #a9cfe6 40%, #d7e8f3 70%, #b8c8d6 100%); }

  /* service tiles */
  .tiles { left: 0; top: 420px; width: 857px; height: 178px; display: flex; }
  .tile { flex: 1; padding: 20px 20px 0; color: var(--white); position: relative; }
  .tile h2 { font-size: 17px; font-weight: 400; letter-spacing: 1.4px; margin-bottom: 14px; }
  .tile p { font-size: 9.5px; line-height: 18px; letter-spacing: 0.8px; text-align: justify; }
  .tile .btn { position: absolute; left: 20px; top: 132px; }
  .tile-sky { background: var(--tile-sky); }
  .tile-ocean { background: var(--tile-ocean); }
  .tile-indigo { background: var(--tile-indigo); }
  .tile-violet { background: var(--tile-violet); }

  .btn { display: inline-flex; align-items: center; gap: 6px; height: 28px; padding: 0 10px; border: 1px solid currentColor; font-size: 9.5px; letter-spacing: 0.8px; color: inherit; text-decoration: none; }
  .btn svg { width: 12px; height: 10px; }
  .btn-light { color: var(--white); }
  .btn-dark { color: #8a8a8a; border-color: #8a8a8a; }

  /* content columns */
  .column { top: 640px; width: 262px; }
  .column h3 { font-size: 16px; font-weight: 400; letter-spacing: 1.3px; color: var(--text-dark); padding-bottom: 12px; border-bottom: 2px solid var(--date-blue); height: 34px; }
  .post-head { display: flex; align-items: center; margin-top: 18px; height: 56px; }
  .post-date { width: 62px; height: 56px; background: var(--date-blue); color: var(--white); font-size: 14px; font-weight: 600; display: flex; align-items: center; justify-content: center; flex: none; }
  .post-title { margin-left: 8px; font-size: 14.5px; font-weight: 400; letter-spacing: 1px; color: var(--brand-blue); line-height: 18px; }
  .post-photo { width: 262px; height: 176px; margin-top: 11px; }
  .post-author { font-size: 11px; font-style: italic; letter-spacing: 1px; color: var(--text-muted); margin-top: 4px; }
  .post-text { font-size: 12.5px; line-height: 18px; letter-spacing: 0.9px; text-align: justify; color: var(--text-body); margin: 2px 0 18px; }

  .col-news { left: 16px; }
  .col-advice { left: 306px; }
  .col-advice h3 { margin-top: -2px; }

  .photo-doctor { background: linear-gradient(135deg, #e6e4e2 0%, #f4f1ee 50%, #c9c6c4 100%); }
  .photo-beach { background: linear-gradient(180deg, #6fb3e0 0%, #8fc9e8 45%, #4fb8b8 75%, #e8e2cf 100%); }
  .photo-webinar { background: linear-gradient(180deg, #0a0a0c 0%, #141420 60%, #1c3f8a 100%); }

  .divider { left: 592px; top: 624px; width: 4px; height: 552px; background: #e3e3e3; box-shadow: 1px 0 3px rgba(0,0,0,0.08); }

  .sidebar { left: 614px; top: 640px; width: 232px; }
  .sidebar h3 { font-size: 16px; font-weight: 400; letter-spacing: 1.3px; color: var(--text-dark); line-height: 18px; margin-left: 4px; }
  .field { display: block; width: 228px; height: 32px; margin-top: 8px; border: 1px solid var(--input-border); box-shadow: inset 0 2px 4px rgba(0,0,0,0.06); font-family: inherit; font-size: 11.5px; font-weight: 300; letter-spacing: 0.6px; color: #b0b0b0; padding-left: 12px; background: var(--white); }
  .field-first { margin-top: 10px; }
  .webinars-title { margin-top: 36px; }
  .webinar-link { font-size: 13px; font-weight: 400; letter-spacing: 1px; line-height: 18px; color: var(--brand-blue); margin: 12px 0 0 4px; }
  .webinar-photo { width: 228px; height: 131px; margin: 8px 0 0 2px; }
  .webinar-text { font-size: 12.5px; line-height: 18px; letter-spacing: 0.9px; text-align: justify; margin: 6px 0 0 2px; width: 228px; }
</style>
</head>
<body>

<header>
  <div class="brand abs">
    <span class="brand-mark"></span>
    <div class="brand-name">JuniperLab</div>
    <div class="brand-tagline">Next Generation Pathology Consultants</div>
  </div>

  <div class="social abs" aria-label="Social links">
    <span></span><span></span><span></span><span></span>
  </div>
  <div class="account-links abs">REGISTER<span class="sep">|</span>SIGN IN</div>

  <nav class="main-nav abs">
    <a href="#">HOME</a>
    <a href="#" class="active">TEST MENU</a>
    <a href="#">RESULTS</a>
    <a href="#">ORDER SERVICES</a>
    <a href="#">CONTACT</a>
  </nav>
  <div class="header-rule abs"></div>
</header>

<div class="hero abs" role="img" aria-label="Pathologist in mask and gloves looking through a microscope in a lab"></div>

<section class="tiles abs">
  <div class="tile tile-sky">
    <h2>Speak With Us</h2>
    <p>If you would like to speak with one of our pathologists, contact us on online, by email or by phone</p>
    <a href="#" class="btn btn-light">Read more <svg viewBox="0 0 12 10"><path d="M0 5h10M6 1l4 4-4 4" fill="none" stroke="currentColor" stroke-width="1.5"/></svg></a>
  </div>
  <div class="tile tile-ocean">
    <h2>Results</h2>
    <p>You can check your results online by using our online checking system.</p>
    <a href="#" class="btn btn-light">Read more <svg viewBox="0 0 12 10"><path d="M0 5h10M6 1l4 4-4 4" fill="none" stroke="currentColor" stroke-width="1.5"/></svg></a>
  </div>
  <div class="tile tile-indigo">
    <h2>Education</h2>
    <p>View our educational material and webinars online. Participate and share your comments/questions at the end of the webinar.</p>
    <a href="#" class="btn btn-light">Read more <svg viewBox="0 0 12 10"><path d="M0 5h10M6 1l4 4-4 4" fill="none" stroke="currentColor" stroke-width="1.5"/></svg></a>
  </div>
  <div class="tile tile-violet">
    <h2>Create An Account</h2>
    <p>Set up anew account with JuniperLab and have your records easily accessible to you via our web portal.</p>
    <a href="#" class="btn btn-light">Read more <svg viewBox="0 0 12 10"><path d="M0 5h10M6 1l4 4-4 4" fill="none" stroke="currentColor" stroke-width="1.5"/></svg></a>
  </div>
</section>

<section class="column col-news abs">
  <h3>News From Our Doctors</h3>
  <div class="post-head">
    <div class="post-date">03 Apr</div>
    <div class="post-title">Avoiding Disease -<br>Watch What you Eat</div>
  </div>
  <div class="post-photo photo-doctor" role="img" aria-label="Smiling doctor in a white coat beside a microscope"></div>
  <div class="post-author">Authur - Clara Wendholt</div>
  <p class="post-text">Clara Wendholt tells us the 5 ways to help avoid contracting diseases through what we eat.</p>
  <a href="#" class="btn btn-dark">Read more <svg viewBox="0 0 12 10"><path d="M0 5h10M6 1l4 4-4 4" fill="none" stroke="currentColor" stroke-width="1.5"/></svg></a>
</section>

<section class="column col-advice abs">
  <h3>Advice From the Expert</h3>
  <div class="post-head">
    <div class="post-date">01 Apr</div>
    <div class="post-title">20 Great Locations to<br>Travel Without the<br>Stress</div>
  </div>
  <div class="post-photo photo-beach" role="img" aria-label="Tropical beach with palm trees, a hammock and a lagoon"></div>
  <div class="post-author">Authur - Marcus Ellery</div>
  <p class="post-text">Trying to find a location that doesn’t invovle the risk of Dengue Fever or other critical diseases? Marcus Ellery has a list of 20 amazing locations for you to go where you won’t have the stress of ......</p>
  <a href="#" class="btn btn-dark">Read more <svg viewBox="0 0 12 10"><path d="M0 5h10M6 1l4 4-4 4" fill="none" stroke="currentColor" stroke-width="1.5"/></svg></a>
</section>

<div class="divider abs"></div>

<aside class="sidebar abs">
  <h3>Sign up For<br>Our Newsletter</h3>
  <input class="field field-first" type="text" placeholder="enter your name">
  <input class="field" type="text" placeholder="enter your email address">
  <h3 class="webinars-title">Recent Webinars</h3>
  <div class="webinar-link">Nora Lindqvist-Education System Needs to Change</div>
  <div class="webinar-photo photo-webinar" role="img" aria-label="Speaker on a dark stage addressing an audience"></div>
  <p class="webinar-text">Nora Lindqvist speaks to the audience about the importance of how the education system needs to provide our children with more knowledge on the importance of......</p>
</aside>

</body>
</html>
```